Book cover design, title is "Chart Your Own Path: How to Build a Solo Career in 10 Months"

Design a cover for a book about freelancing. Example of my previous book's cover attached. Book title is "Chart Your Own Path: How to Build a Solo Career in 10 Months". Looking to target people who have a 9-5 job but are seeking to try out freelancing as a way to supplement income and eventually quit their day job.

Target Market(s)

Looking to target people who have a 9-5 job but are seeking to try out freelancing as a way to supplement income and eventually quit their day job.

Industry/Entity Type

Consulting

Font styles to use
Serif
Sans Serif

Colors

Designer to choose colors to be used in the design.

Requirements
Must have
• I love these books covers...
• https://www.pagewharf.example/Tame-Notebin-Informal-Sorting-Handling-ebook/dp/Q71MZTRQWO/ref=asap_bc?ie=UTF8
• https://www.pagewharf.example/Wonder-Dawn-Authors-Drafting-Improves/dp/5830417726/ref=asap_bc?ie=UTF8
• https://www.pagewharf.example/Ways-Draft-Factbook-eBook-Weeks-ebook/dp/Q44KT29ZP8/ref=asap_bc?ie=UTF8
• https://www.pagewharf.example/Routine-Layering-Minor-Shifts-Moments/dp/5820763915/ref=asap_bc?ie=UTF8
• https://www.pagewharf.example/Boost-Each-Hour-Core-ebook/dp/Q93WNV6HLC/ref=asap_bc?ie=UTF8
• https://www.pagewharf.example/Maker-Co-Complete-Thriving-Solo-ebook/dp/Q66218FJXR/ref=sr_1_4?ie=UTF8&qid=1620583947&sr=8-4&keywords=freelancing
Should not have
• Don't submit 3D renderings, just the front cover image please.

```html
<!DOCTYPE html>
<html lang="en">
<head>
<meta charset="utf-8">
<title>Chart Your Own Path – Book Cover</title>
<link rel="stylesheet" href="https://fonts.googleapis.com/css2?family=Josefin+Sans:wght@700&family=Poiret+One&display=swap">
<style>
  :root {
    --page-bg: #efe4d6;
    --cover-top: #f07a0c;
    --cover-mid: #f28a12;
    --cover-bottom: #fcc42c;
    --ink-light: #ffffff;
    --photo-warm: rgba(214, 128, 24, 0.28);
  }
  * { margin: 0; padding: 0; box-sizing: border-box; }
  html, body {
    width: 1200px;
    height: 960px;
    overflow: hidden;
    background: var(--page-bg);
  }
  .stage {
    position: relative;
    width: 1200px;
    height: 960px;
  }
  .book-cover {
    position: absolute;
    left: 305px;
    top: 40px;
    width: 590px;
    height: 880px;
    overflow: hidden;
    background: linear-gradient(180deg, var(--cover-top) 0%, var(--cover-mid) 45%, var(--cover-bottom) 100%);
    box-shadow: 0 14px 36px rgba(80, 40, 0, 0.28);
    color: var(--ink-light);
    text-align: center;
  }
  .cover-title {
    position: absolute;
    top: 72px;
    left: 0;
    width: 100%;
    font-family: "Josefin Sans", sans-serif;
    font-weight: 700;
    font-size: 76px;
    line-height: 88px;
    letter-spacing: 0.5px;
    text-transform: uppercase;
  }
  .cover-title span { display: block; }
  .cover-subtitle {
    position: absolute;
    top: 402px;
    left: 0;
    width: 100%;
    font-family: "Poiret One", sans-serif;
    font-size: 38px;
    line-height: 56px;
    letter-spacing: 1px;
    text-transform: uppercase;
  }
  .cover-subtitle span { display: block; }
  .cover-photo {
    position: absolute;
    left: 0;
    top: 560px;
    width: 100%;
    height: 320px;
    background: linear-gradient(180deg, rgba(214, 128, 24, 0) 0%, var(--photo-warm) 55%, rgba(214, 128, 24, 0.12) 100%);
  }
  .cover-author {
    position: absolute;
    left: 0;
    top: 829px;
    width: 100%;
    font-family: "Josefin Sans", sans-serif;
    font-weight: 700;
    font-size: 21px;
    letter-spacing: 0.5px;
    text-transform: uppercase;
  }
</style>
</head>
<body>
  <main class="stage">
    <section class="book-cover">
      <h1 class="cover-title">
        <span>Chart Your</span>
        <span>Own Path</span>
      </h1>
      <p class="cover-subtitle">
        <span>How to Build a Solo</span>
        <span>Career in 10 Months</span>
      </p>
      <div class="cover-photo" role="img" aria-label="Photo of two glasses of red wine clinking in a toast, with a lit candle softly blurred behind"></div>
      <p class="cover-author">Writers Name</p>
    </section>
  </main>
</body>
</html>
```